UK based Drone services needs a pdf / flyer designed.

I am looking to get a flyer advertising what we do. I have added a word document with a little background and what services we offer, please could you add images for each service if possible? We are BPN approved and would like that to be mentioned on the bottom right corner please (logo attached). All our work is carried out with QVO drones, so would ideally like maybe a QVO Talvren 820 rtk image in there. Brantiqo is the name of the company. Please get back to me if you have any questions.

```html
<!DOCTYPE html>
<html lang="en">
<head>
<meta charset="utf-8">
<title>Brantiqo Drone Services Flyer</title>
<link rel="stylesheet" href="https://fonts.googleapis.com/css2?family=Bebas+Neue&family=Oswald:wght@300;400;500;600&family=Montserrat:wght@400;500&display=swap">
<style>
:root{
  --backdrop:#c4c4c4;
  --paper:#f4f4f4;
  --navy:#0d2449;
  --blue:#4a78b4;
  --blue-light:#8fb0dc;
  --ink:#2b2b2b;
  --heading:#1f2d45;
  --black:#0b0b0b;
  --charcoal:#323232;
  --white:#ffffff;
}
*{margin:0;padding:0;box-sizing:border-box}
html,body{width:977px;height:1200px;overflow:hidden}
body{background:var(--backdrop);position:relative;font-family:"Montserrat",sans-serif}
.flyer{position:absolute;left:135px;top:100px;width:707px;height:1000px;background:var(--paper);overflow:hidden;box-shadow:0 4px 18px rgba(0,0,0,.25)}
.hero-art{position:absolute;left:0;top:0}
.brand{position:absolute;left:60px;top:70px;width:190px;text-align:center;font-family:"Oswald",sans-serif;font-weight:500;font-size:42px;color:#3a3a3a;letter-spacing:1px}
.headline-box{position:absolute;left:0;top:176px;width:287px;height:171px;background:rgba(70,70,70,.55)}
.headline-box::before{content:"";position:absolute;left:40px;top:11px;width:2px;height:148px;background:#2a2a2a}
.headline{position:absolute;left:49px;top:8px;color:var(--white);text-transform:uppercase;white-space:nowrap}
.headline .thin{display:block;font-family:"Oswald",sans-serif;font-weight:300;font-size:34px;line-height:38px;letter-spacing:-1px}
.headline .bold{display:block;font-family:"Bebas Neue",sans-serif;font-weight:400;font-size:45px;line-height:38px;letter-spacing:-.3px}
.body-copy{position:absolute;left:21px;font-size:11.8px;line-height:14.3px;color:var(--ink)}
.body-copy p{position:relative;padding-left:20px;text-align:justify}
.body-copy p::before{content:"";position:absolute;left:0;top:0;width:15px;height:15px;border-radius:50%;background:var(--blue)}
.body-copy p::after{content:"";position:absolute;left:4px;top:4.5px;width:4px;height:4px;border-right:1.5px solid #fff;border-top:1.5px solid #fff;transform:rotate(45deg)}
.copy-intro{top:444px;width:355px}
.copy-equipped{top:657px;width:659px}
.copy-pride{top:707px;width:659px}
.services-band{position:absolute;left:0;top:789px;width:707px;height:106px;background:linear-gradient(90deg,#3f6aa3,#5b87c0 50%,#3f6aa3)}
.services-tab{position:absolute;left:0;top:767px;width:272px;height:48px;background:linear-gradient(#f2f2f2,#d8d8d8);clip-path:polygon(0 0,262px 0,272px 48px,0 48px)}
.services-title{position:absolute;left:28px;top:0;font-family:"Bebas Neue",sans-serif;font-weight:400;font-size:38px;line-height:50px;color:var(--heading);white-space:nowrap}
.service-icon{position:absolute;top:821px;width:68px;height:68px;border-radius:50%;background:radial-gradient(circle at 40% 35%,#ffffff,#c9c9c9 60%,#8d8d8d);box-shadow:0 2px 4px rgba(0,0,0,.4);display:flex;align-items:center;justify-content:center}
.service-icon svg{width:40px;height:40px;stroke:#222;fill:none;stroke-width:2.4;stroke-linecap:round;stroke-linejoin:round}
.labels-band{position:absolute;left:0;top:895px;width:707px;height:29px;background:var(--black)}
.service-label{position:absolute;top:0;height:29px;width:110px;display:flex;align-items:center;justify-content:center;text-align:center;font-family:"Oswald",sans-serif;font-weight:500;font-size:9.5px;line-height:10.5px;color:var(--white);text-transform:uppercase}
.footer-strip{position:absolute;left:0;top:924px;width:707px;height:22px;background:var(--blue)}
.footer-right{position:absolute;left:0;top:946px;width:707px;height:54px;background:var(--charcoal)}
.footer-left{position:absolute;left:0;top:924px;width:314px;height:76px;background:var(--white);clip-path:polygon(0 0,295px 0,314px 76px,0 76px)}
.footer-left::after{content:"";position:absolute;inset:0;background:var(--navy);clip-path:polygon(0 0,288px 0,306px 76px,0 76px)}
.contact{position:absolute;display:flex;align-items:center;gap:8px;font-family:"Oswald",sans-serif;color:var(--white);text-transform:uppercase;white-space:nowrap}
.contact .dot{width:18px;height:18px;border-radius:50%;background:#e6e6e6;display:flex;align-items:center;justify-content:center;flex:none}
.contact .dot svg{width:11px;height:11px;fill:none;stroke:#333;stroke-width:2}
.contact-address{left:22px;top:934px;font-size:15px}
.contact-phone{left:22px;top:961px;font-size:15px}
.contact-fax{left:132px;top:961px;font-size:15px}
.contact-web{left:318px;top:962px;font-size:10px;letter-spacing:.5px}
.contact-mail{left:448px;top:962px;font-size:10px;letter-spacing:.5px}
.approval-badge{position:absolute;left:627px;top:922px;width:53px;height:58px;border-radius:4px;background:linear-gradient(#ffffff,#dcdcdc);box-shadow:0 1px 3px rgba(0,0,0,.5)}
.approval-badge::after{content:"";position:absolute;left:6px;top:6px;right:6px;bottom:6px;border-radius:2px;background:#2f63a8}
</style>
</head>
<body>
<main class="flyer">
  <svg class="hero-art" width="707" height="640" viewBox="0 0 707 640">
    <defs>
      <linearGradient id="cityTone" x1="0" y1="0" x2="1" y2="1">
        <stop offset="0" stop-color="#f2f2f2"/>
        <stop offset=".45" stop-color="#9a9a9a"/>
        <stop offset="1" stop-color="#5c5c5c"/>
      </linearGradient>
      <linearGradient id="sunsetTone" x1="0" y1="0" x2="0" y2="1">
        <stop offset="0" stop-color="#f0a53a"/>
        <stop offset=".5" stop-color="#d97d1c"/>
        <stop offset="1" stop-color="#5a3a24"/>
      </linearGradient>
      <linearGradient id="fieldTone" x1="0" y1="0" x2="0" y2="1">
        <stop offset="0" stop-color="#4fb0df"/>
        <stop offset=".5" stop-color="#e6dccb"/>
        <stop offset="1" stop-color="#d9b978"/>
      </linearGradient>
    </defs>
    <rect width="707" height="440" fill="url(#cityTone)" role="img" aria-label="Greyscale photo of a city skyline with a drone in the sky"/>
    <path d="M0 430 Q200 360 400 372 L707 372 L707 640 L0 640 Z" fill="var(--paper)"/>
    <path d="M0 415 Q200 355 400 362 L400 372 Q200 366 0 430 Z" fill="var(--blue)"/>
    <circle cx="557" cy="315" r="212" fill="#8fb0dc"/>
    <circle cx="557" cy="315" r="204" fill="var(--blue)"/>
    <circle cx="563" cy="318" r="193" fill="#ffffff"/>
    <circle cx="568" cy="320" r="185" fill="url(#sunsetTone)" role="img" aria-label="QVO Talvren 820 rtk drone flying over a city at sunset"/>
    <circle cx="571" cy="525" r="100" fill="#d6d6d6"/>
    <circle cx="571" cy="525" r="95" fill="url(#fieldTone)" role="img" aria-label="Pilot holding a small drone in a wheat field"/>
  </svg>

  <div class="brand">Brantiqo</div>

  <div class="headline-box">
    <h1 class="headline">
      <span class="thin">Photography,</span>
      <span class="thin">Videography,</span>
      <span class="bold">&amp; Inspection</span>
      <span class="bold">Drone Services.</span>
    </h1>
  </div>

  <div class="body-copy copy-intro">
    <p>Unmanned Arial Vehicles (UAV's) are revolutionizing the way industries are able to work. With current advances in technology, drones are opening doors that weren't available before. With the ability to reach difficult and dangerous areas, they remove the human element and change the scope of what's safely possible. Capturing live Ultra High-Definition footage of unreachable areas and making working at heights a thing of the past. Drones are safer, faster, more cost-effective and a highly accurate alternative. Not only do you have the chance to inspect dangerous areas live, but you also get photographs and/or 4K Ultra HD video footage to review at a later date. No need to send someone back out to the area to double-check damage, you have it all on record.</p>
  </div>
  <div class="body-copy copy-equipped">
    <p>Brantiqo is fully equipped with the latest and most suitable drones for your business or personal needs. From a small roof survey to a full wind turbine site inspection. No project is too small or too large, take advantage of using UAV's now!</p>
  </div>
  <div class="body-copy copy-pride">
    <p>Here at Brantiqo, we pride ourselves on being affordable and offering a great product to our clients. We have a comprehensive list of services that we offer to any business or individual across the UK. Our UAV pilots are GVC licensed and have gained Operational Authorization from the BPN allowing us to carry out commercial work in the UK.</p>
  </div>

  <div class="services-band"></div>
  <div class="services-tab"><h2 class="services-title">SERVICES WE OFFER</h2></div>

  <div class="service-icon" style="left:45px"><svg viewBox="0 0 40 40"><circle cx="11" cy="25" r="7"/><circle cx="29" cy="25" r="7"/><path d="M14 13h12M17 25h6M6 20l5-8M34 20l-5-8"/></svg></div>
  <div class="service-icon" style="left:155px"><svg viewBox="0 0 40 40"><path d="M5 9l9-4 10 4 10-4v24l-10 4-10-4-9 4z"/><circle cx="26" cy="24" r="5"/><path d="M30 28l5 5"/></svg></div>
  <div class="service-icon" style="left:264px"><svg viewBox="0 0 40 40"><rect x="6" y="9" width="28" height="24" rx="3"/><path d="M6 15h28M17 20v9l7-4.5z"/></svg></div>
  <div class="service-icon" style="left:374px"><svg viewBox="0 0 40 40"><path d="M8 16h24l4 12H4z M12 16l-2 12M20 16v12M28 16l2 12M6 22h28M20 28v7M14 35h12"/><circle cx="20" cy="8" r="3"/></svg></div>
  <div class="service-icon" style="left:484px"><svg viewBox="0 0 40 40"><path d="M8 17l12-10 12 10M12 14v10M28 14v10M8 28l6-3 6 4 6-4 6 3M13 31l7 4 7-4"/></svg></div>
  <div class="service-icon" style="left:594px"><svg viewBox="0 0 40 40"><circle cx="11" cy="27" r="6"/><circle cx="31" cy="29" r="4"/><path d="M6 20V12h12l3 8h12v9M24 20V10"/></svg></div>

  <div class="labels-band">
    <div class="service-label" style="left:24px">Commercial Inspections</div>
    <div class="service-label" style="left:134px">Mapping / Surveys</div>
    <div class="service-label" style="left:243px">Arial Photography \<br>Videography</div>
    <div class="service-label" style="left:353px">Solar Panel Inspections</div>
    <div class="service-label" style="left:463px">Real Estate / Planning</div>
    <div class="service-label" style="left:573px">Agriculture</div>
  </div>

  <div class="footer-strip"></div>
  <div class="footer-right"></div>
  <div class="footer-left"></div>

  <div class="contact contact-address"><span class="dot"><svg viewBox="0 0 12 12"><path d="M6 11s-4-4-4-6.5a4 4 0 0 1 8 0C10 7 6 11 6 11z"/><circle cx="6" cy="4.5" r="1.2"/></svg></span>1900 St. Dummy Text, Dummy Text, TX</div>
  <div class="contact contact-phone"><span class="dot"><svg viewBox="0 0 12 12"><path d="M2.5 1.5l2 2-1 1.5c.8 1.6 1.9 2.7 3.5 3.5l1.5-1 2 2-1.5 1.5C5 10.5 1.5 7 1 2.5z"/></svg></span>123 456 789</div>
  <div class="contact contact-fax"><span class="dot"><svg viewBox="0 0 12 12"><rect x="2" y="4" width="8" height="6"/><path d="M4 4V1h4v3"/></svg></span>123 456 789</div>
  <div class="contact contact-web"><span class="dot"><svg viewBox="0 0 12 12"><circle cx="6" cy="6" r="4.5"/><path d="M1.5 6h9M6 1.5c-2 3-2 6 0 9M6 1.5c2 3 2 6 0 9"/></svg></span>www.brantiqo.com</div>
  <div class="contact contact-mail"><span class="dot"><svg viewBox="0 0 12 12"><rect x="1.5" y="3" width="9" height="6"/><path d="M1.5 3l4.5 3.5L10.5 3"/></svg></span>info@brantiqo.com</div>

  <div class="approval-badge" role="img" aria-label="BPN approval badge"></div>
</main>
</body>
</html>
```